Wine Label Design for the red wine named “Amber Over Stone” or “A/S”

Create an elegant yet simple (less is more) label for a red, full-bodied wine from a family-owned Herzegovinian vineyard by the river with 9 names. You can use elements such as the Calopteryx virgo, possibly the river shape, and ensure a coherent storytelling of the unique vineyard’s locality and meticulous, hand-picked grape cultivation.
Let’s craft a label that is not just seen, but is experienced and remembered.

Target Market(s)

Wine lovers that appreciate high quality wines

Industry/Entity Type

Wine, Family owned small producer

Requirements
Must have
• Name A/S, front and back label. Premium feel, uniqueness. Simple but interesting.
Nice to have
• Please see the images below as an idea of various directions. I am also leaning to embossed image on the label
Should not have
• Should not be overcrowded with text, too many images and objects

```html
<!DOCTYPE html>
<html lang="en">
<head>
<meta charset="utf-8">
<title>A/S Wine – Front Label Spec Sheet</title>
<link rel="stylesheet" href="https://fonts.googleapis.com/css2?family=Source+Sans+3:wght@400;600&display=swap">
<style>
  :root {
    --paper: #e7e8e9;
    --rule: #8d8e90;
    --bar: #939598;
    --tab-light: #d6d8d9;
    --ink: #1a1a1a;
    --die: #e3262b;
    --white: #ffffff;
    --black: #000000;
    --emboss-deep: #2b2b2c;
  }
  html, body {
    margin: 0;
    padding: 0;
    width: 1200px;
    height: 3299px;
    overflow: hidden;
    background: var(--paper);
  }
  .spec-sheet {
    display: block;
    width: 1200px;
    height: 3299px;
    font-family: "Source Sans 3", "Myriad Pro", Arial, sans-serif;
  }
  .rule { stroke: var(--rule); stroke-width: 1; fill: none; }
  .crop { stroke: #3a3a3a; stroke-width: 1; }
  .bar { fill: var(--bar); }
  .bar-text { fill: var(--white); font-size: 11.5px; }
  .tab-text { fill: var(--ink); font-size: 14px; }
  .side-tab-text { fill: var(--ink); font-size: 9.5px; }
  .label-key { fill: var(--ink); font-size: 9px; }
  .label-value { fill: var(--ink); font-size: 12px; }
  .small-bold { fill: var(--ink); font-size: 8px; font-weight: 600; }
  .small { fill: var(--ink); font-size: 7.5px; }
  .swatch-text { fill: var(--ink); font-size: 10px; }
  .dimension { fill: var(--ink); font-size: 10px; }
  .brand-name { fill: var(--ink); font-size: 27px; font-weight: 400; }
  .layer-label { fill: var(--ink); font-size: 11px; letter-spacing: 0.3px; }
  .die-line { fill: none; stroke: var(--die); stroke-width: 1; }
  .print-area { fill: var(--black); }
</style>
</head>
<body>
<svg class="spec-sheet" viewBox="0 0 794 2183" width="1200" height="3299" xmlns="http://www.w3.org/2000/svg">
  <defs>
    <radialGradient id="emboss-tone" cx="0.55" cy="0.42" r="0.6">
      <stop offset="0" stop-color="var(--emboss-deep)" stop-opacity="0.85"/>
      <stop offset="0.55" stop-color="var(--emboss-deep)" stop-opacity="0.35"/>
      <stop offset="1" stop-color="var(--paper)" stop-opacity="0"/>
    </radialGradient>
  </defs>

  <!-- Header: title block -->
  <g class="title-block">
    <path class="rule" d="M33 46 V27 H193 L200 46" fill="var(--paper)"/>
    <text class="tab-text" x="41" y="41">Label Design</text>

    <rect class="bar" x="33" y="46" width="592" height="21"/>
    <text class="bar-text" x="270" y="61" text-anchor="middle">Date: 09. October 2023</text>
    <text class="bar-text" x="523" y="61" text-anchor="middle">Realesed: 10. November 2023</text>

    <path d="M615 46 H741 L750 67 H624 Z" fill="var(--tab-light)" stroke="var(--rule)" stroke-width="1"/>
    <text class="side-tab-text" x="685" y="60" text-anchor="middle">Dimension Label Design</text>

    <rect class="rule" x="33" y="67" width="717" height="183"/>
    <line class="rule" x1="624" y1="67" x2="624" y2="250"/>
    <line class="rule" x1="329" y1="75" x2="329" y2="222"/>
    <line class="rule" x1="432" y1="75" x2="432" y2="222"/>
    <line class="rule" x1="329" y1="136" x2="624" y2="136"/>
    <line class="rule" x1="50" y1="222" x2="624" y2="222"/>

    <text class="brand-name" x="92" y="115" text-anchor="middle">A/S</text>

    <text class="label-key" x="55" y="157">DESIGN:</text>
    <text class="label-value" x="97" y="157">Wine label front</text>
    <text class="label-key" x="55" y="180">NAME:</text>
    <text class="label-value" x="97" y="180">A/S Wine</text>
    <text class="small-bold" x="55" y="195">Software / Version: Vector Studio 6</text>

    <text class="label-key" x="379" y="115" text-anchor="middle">Designer:</text>

    <rect x="458" y="78" width="28" height="14" fill="var(--white)" stroke="var(--black)" stroke-width="1"/>
    <rect x="458" y="97" width="28" height="14" fill="var(--black)"/>
    <text class="swatch-text" x="505" y="89">#&#160;FFFFFF</text>
    <text class="swatch-text" x="505" y="107">#&#160;000000</text>

    <text class="small" x="437" y="154">- Textured paper ( color)Permanent</text>
    <text class="small" x="439" y="164">waterproof adhesive</text>
    <text class="small" x="437" y="180">- Paper thickness - 90 lb</text>
    <text class="small" x="437" y="195">- Embossed stamp</text>

    <text class="small" x="52" y="242">Fonts: Scripta Pro-Bold, Times</text>

    <text class="dimension" x="653" y="112">W = 90 mm</text>
    <text class="dimension" x="653" y="126">H = 100 mm</text>
    <rect class="die-line" x="656" y="162" width="53" height="59"/>
  </g>

  <!-- Layer 1: die cut -->
  <g class="layer layer-die-cut">
    <g class="crop-marks">
      <line class="crop" x1="265" y1="300" x2="265" y2="324"/>
      <line class="crop" x1="520" y1="300" x2="520" y2="324"/>
      <line class="crop" x1="265" y1="633" x2="265" y2="657"/>
      <line class="crop" x1="520" y1="633" x2="520" y2="657"/>
      <line class="crop" x1="229" y1="338" x2="253" y2="338"/>
      <line class="crop" x1="533" y1="338" x2="557" y2="338"/>
      <line class="crop" x1="229" y1="620" x2="253" y2="620"/>
      <line class="crop" x1="533" y1="620" x2="557" y2="620"/>
    </g>
    <rect class="die-line" x="265" y="338" width="255" height="282"/>
    <line class="crop" x1="583" y1="463" x2="631" y2="463"/>
    <text class="layer-label" x="646" y="467">DIE CUT</text>
  </g>

  <!-- Layer 2: print -->
  <g class="layer layer-print">
    <g class="crop-marks">
      <line class="crop" x1="265" y1="725" x2="265" y2="749"/>
      <line class="crop" x1="520" y1="725" x2="520" y2="749"/>
      <line class="crop" x1="265" y1="1058" x2="265" y2="1082"/>
      <line class="crop" x1="520" y1="1058" x2="520" y2="1082"/>
      <line class="crop" x1="229" y1="762" x2="253" y2="762"/>
      <line class="crop" x1="533" y1="762" x2="557" y2="762"/>
      <line class="crop" x1="229" y1="1045" x2="253" y2="1045"/>
      <line class="crop" x1="533" y1="1045" x2="557" y2="1045"/>
    </g>
    <rect class="print-area" x="265" y="762" width="255" height="283"/>
    <line class="crop" x1="583" y1="908" x2="631" y2="908"/>
    <text class="layer-label" x="646" y="912">PRINT</text>
  </g>

  <!-- Layer 3: embossed stamp -->
  <g class="layer layer-emboss">
    <g class="crop-marks">
      <line class="crop" x1="265" y1="1174" x2="265" y2="1198"/>
      <line class="crop" x1="520" y1="1174" x2="520" y2="1198"/>
      <line class="crop" x1="265" y1="1510" x2="265" y2="1534"/>
      <line class="crop" x1="520" y1="1510" x2="520" y2="1534"/>
      <line class="crop" x1="229" y1="1211" x2="253" y2="1211"/>
      <line class="crop" x1="533" y1="1211" x2="557" y2="1211"/>
      <line class="crop" x1="229" y1="1497" x2="253" y2="1497"/>
      <line class="crop" x1="533" y1="1497" x2="557" y2="1497"/>
    </g>
    <text class="brand-name" x="330" y="1272" text-anchor="middle">A/S</text>
    <rect class="emboss-illustration" x="334" y="1296" width="116" height="146"
          fill="url(#emboss-tone)" role="img"
          aria-label="Embossed black illustration of a banded demoiselle dragonfly, wings swept up to the right and long slender body trailing down to the lower right"/>
    <line class="crop" x1="583" y1="1357" x2="631" y2="1357"/>
    <text class="layer-label" x="646" y="1361">EMBOSSED&#160; STAMP</text>
  </g>
</svg>
</body>
</html>
```